Chinese citizens moving to SYDNEY!

We need an A5 size flier for our new business. We would like this to be a fold-out flyer (brochure-style, i.e. 4 sides - front cover, middle, back cover). Full colour print (or 4 colour if it can be done without compromising the look). We need two versions of the same flyer - one in Chinese and one in English. Same design and imagery, just different languages. Copy is attached with imagery (subject to change once we source high res images).

Target Market(s)

Chinese citizens looking to emigrate to Sydney AND Chinese citizens who have recently moved to Sydney.

Industry/Entity Type

Business

Font styles to use
Sans Serif

Colors
ec1f27
000000
ffffff
fece3e

Requirements
Must have
• The front cover of the flier must be clean looking and show just our business name and tag line, along with an image of Sydney Harbour (provided). Main information ideally to be spread across the 2 centre pages with the back page quite clean, but if the text is too small we could consider it being spread across the remaining 3 pages (i.e. centre of the brochure, then the back cover).
• We would like it to be a clean and easy to read design. Suggested colours are written in the brief.
• It would be ideal to have a designer who can read Mandarin so that they know which characters make up a headline, which characters should not be spaced over two rows of text etc.

```html
<!DOCTYPE html>
<html lang="en">
<head>
<meta charset="utf-8">
<title>Harbour Light Concierge – Brochure</title>
<link rel="stylesheet" href="https://fonts.googleapis.com/css2?family=Oswald:wght@400;500;600;700&family=Lato:wght@400;700&display=swap">
<style>
  :root{
    --red:#ec1f27;
    --yellow:#fece3e;
    --grey:#838383;
    --ink:#3a3a3a;
    --heading:#555555;
    --white:#ffffff;
    --photo-sky:#8fb6dc;
    --photo-steel:#4a5a6e;
    --photo-water:#3d6fa8;
  }
  *{box-sizing:border-box;margin:0;padding:0}
  html,body{width:1200px;height:965px;overflow:hidden;background:var(--white)}
  body{position:relative;font-family:"Lato",sans-serif;color:var(--ink)}

  .page{position:absolute;top:87px;width:532px;height:746px;background:var(--white);overflow:hidden}
  .cover{left:39px}
  .inside{left:625px}

  /* Cover */
  .cover-art{position:absolute;left:0;top:0;width:532px;height:425px}
  .cover-brand{position:absolute;top:450px;width:100%;text-align:center;font-family:"Oswald",sans-serif;font-weight:500;font-size:42px;color:var(--heading);letter-spacing:.3px}
  .cover-tagline{position:absolute;top:515px;width:100%;text-align:center;font-family:"Oswald",sans-serif;font-weight:700;font-size:58px;line-height:59px;color:var(--red);text-transform:uppercase;letter-spacing:1px}
  .cover-band{position:absolute;top:633px;left:0;width:100%;height:54px;background:var(--grey);color:var(--white);text-align:center;font-family:"Oswald",sans-serif;font-weight:500;font-size:46px;line-height:54px;letter-spacing:.5px}
  .cover-web{position:absolute;top:704px;width:100%;text-align:center;font-size:10.5px;letter-spacing:6.2px;color:var(--ink)}

  /* Inside */
  .intro{position:absolute;left:0;top:0;width:100%;height:173px;background:var(--grey);color:var(--white);display:flex;gap:12px;padding:28px 28px 0 34px;font-size:9.6px;line-height:11.7px;text-align:justify}
  .intro-col{flex:1}
  .intro p+p{margin-top:11.7px}

  .services-title{position:absolute;left:31px;top:177px;font-family:"Oswald",sans-serif;font-weight:500;font-size:16px;color:var(--red)}

  .section-pill{position:absolute;left:0;height:19px;background:var(--yellow);border-radius:0 10px 10px 0;font-family:"Oswald",sans-serif;font-weight:500;font-size:15px;line-height:19px;color:#222;padding-left:30px}
  .pill-school{top:201px;width:92px}
  .pill-home{top:385px;width:112px;padding-left:32px}
  .pill-everyday{top:542px;width:162px;padding-left:32px}

  .service-list{position:absolute;display:flex;gap:20px;left:30px;width:480px;font-size:9.6px;line-height:11.7px}
  .service-list ul{list-style:none;flex:1}
  .service-list li{position:relative;padding-left:9px;margin-bottom:6.5px}
  .service-list li::before{content:"";position:absolute;left:0;top:4px;width:4px;height:4px;border-radius:50%;background:var(--red)}
  .list-school{top:226px}
  .list-home{top:411px}
  .list-everyday{top:569px}

  .inside-footer{position:absolute;left:0;top:724px;width:100%;height:22px;background:var(--grey);color:var(--white);text-align:center;font-size:10.5px;line-height:22px;letter-spacing:6.2px}
</style>
</head>
<body>

<section class="page cover">
  <svg class="cover-art" viewBox="0 0 532 425" role="img" aria-label="Photograph of Sydney Harbour Bridge arching over the harbour with the city skyline and opera house">
    <defs>
      <linearGradient id="harbour" x1="0" y1="0" x2="0" y2="1">
        <stop offset="0" stop-color="var(--photo-steel)"/>
        <stop offset=".35" stop-color="var(--photo-sky)"/>
        <stop offset=".72" stop-color="#b9cfe6"/>
        <stop offset="1" stop-color="var(--photo-water)"/>
      </linearGradient>
    </defs>
    <polygon points="0,0 532,0 532,368 0,352" fill="url(#harbour)"/>
    <polygon points="0,357 532,425 0,425" fill="var(--yellow)"/>
    <polygon points="329,395 532,370 532,425" fill="var(--red)"/>
  </svg>
  <h1 class="cover-brand">Harbour Light Concierge</h1>
  <p class="cover-tagline">Sydney’s<br>Relocation and</p>
  <p class="cover-band">Settlement Experts</p>
  <p class="cover-web">harbourlightconcierge.example.com</p>
</section>

<section class="page inside">
  <div class="intro">
    <div class="intro-col">
      <p>Harbour Light Concierge is a premium lifestyle service supporting families who are planning or currently migrating to and investing in Australia.</p>
      <p>Specialising in the city of Sydney, Harbour Light Concierge helps families to feel comfortable and at home as soon as possible.</p>
      <p>Our team of local experts provide support every step of the way – answering questions, providing advice and breaking down the language barrier.</p>
    </div>
    <div class="intro-col">
      <p>Our services are highly customisable to suit the needs of individual families. Whether it’s finding the best school for your children, the help you need in your home, knowing where to buy your favourite groceries or an introduction to a great GP or Specialist – Harbour Light Concierge will cater to your every need.</p>
      <p>Your family will be assigned a professional Personal Assistant who is fluent in both English and Mandarin, making the process of migrating less daunting and more enjoyable.</p>
    </div>
  </div>

  <h2 class="services-title">Our services include but are not limited to:</h2>

  <h3 class="section-pill pill-school">School</h3>
  <div class="service-list list-school">
    <ul>
      <li>Recommend the best schools and<br>childcare centres</li>
      <li>Compare school rankings and academic results</li>
      <li>Arrange private tours of schools and meetings<br>with Principals</li>
      <li>Manage the school application process<br>through to completion</li>
      <li>Assist with starting school, such as purchase of uniforms and textbooks, understanding school procedures and more</li>
    </ul>
    <ul>
      <li>Appoint private tutors to assist with learning English and completing homework assignments</li>
      <li>Organise extra curricular activities, such as piano lessons, tennis lessons and more</li>
      <li>Translate all school correspondence such as</li>
      <li>academic report cards, homework assignments and more</li>
    </ul>
  </div>

  <h3 class="section-pill pill-home">Home &amp; Car</h3>
  <div class="service-list list-home">
    <ul>
      <li>Recommend the best suburbs for families</li>
      <li>Make introductions to Real Estate Agents and support the buying process</li>
      <li>Arrange unpacking and home organisation services</li>
      <li>Assist to purchase furniture and appliances</li>
      <li>Source the best utility companies and organise connection – electricity, gas, water, phone, internet, TV and more</li>
    </ul>
    <ul>
      <li>Appoint staff for your home such as cleaners, gardeners and more</li>
      <li>Compare home insurance options and assist with purchasing</li>
      <li>Assist with car purchasing, leasing and acquiring necessary insurance</li>
    </ul>
  </div>

  <h3 class="section-pill pill-everyday">Everyday Necessities</h3>
  <div class="service-list list-everyday">
    <ul>
      <li>Explain local grocery options such as supermarkets, specialty stores, Asian grocers and more</li>
      <li>Recommend beauty and wellness services such as hair salons, nail parlours, beauty salons and more</li>
      <li>Explain retail shopping options such major shopping centres and luxury brands</li>
      <li>Source quality trades people such as plumbers, electricians, painters and more</li>
    </ul>
    <ul>
      <li>Assist with government registrations such as drivers license, Medicare and more</li>
      <li>Assist to open bank accounts and set up<br>online banking</li>
      <li>Assist to set up memberships – library, gym, golf club and more</li>
      <li>Explain private and public transport options</li>
      <li>Organise private and group language classes</li>
      <li>Translate documents and mail</li>
    </ul>
  </div>

  <footer class="inside-footer">harbourlightconcierge.example.com</footer>
</section>

</body>
</html>
```